UI design needed for a prototype based on wireframe

Hey there.
I need a UI design done on a a prototype application idea before I send it to a programmer. Once designed and programmed the app will move onto a testing faze where it will stay for some time and, I assume, go through several redesign fazes. I have a wireframe mockup and background description so I imagine the design work is pretty straight forward. The app is an activity app that let´s users post different activities that they want to to and post it before a community of users who might be willing to participate. Any features worth mentioning might include Mingleport only log-in, Vantoro routes navigation and star rating system of the user. Besides that I think it´s fairly basic. This app will initially be launched only in vantoro stall because of the test feature of the marketplace.

```html
<!DOCTYPE html>
<html lang="en">
<head>
<meta charset="utf-8">
<title>Activity App</title>
<link rel="stylesheet" href="https://fonts.googleapis.com/css2?family=Roboto:wght@400;500;700&display=swap">
<style>
  :root {
    --status-bg: #1f2b33;
    --bar-bg: #263540;
    --accent: #26b3c9;
    --accent-light: #4fd0e0;
    --page-bg: #e6e6e6;
    --card-bg: #ffffff;
    --ink: #3a3a3a;
    --muted: #8a8a8a;
    --rule: #d6d6d6;
    --movies: #f2c12e;
    --concert: #3c3c3c;
    --hiking: #8e44ad;
  }
  * { box-sizing: border-box; margin: 0; padding: 0; }
  html, body { width: 675px; height: 1200px; overflow: hidden; }
  body { font-family: 'Roboto', sans-serif; background: var(--page-bg); position: relative; color: var(--ink); }

  .status-bar { height: 50px; background: var(--status-bg); display: flex; justify-content: flex-end; align-items: center; gap: 14px; padding-right: 22px; color: #fff; font-size: 24px; }
  .app-bar { height: 85px; background: var(--bar-bg); display: flex; align-items: center; padding: 0 30px; }
  .app-title { color: var(--accent-light); font-size: 36px; font-weight: 500; margin-left: 40px; flex: 1; }
  .tabs { height: 119px; background: var(--bar-bg); display: flex; }
  .tab { flex: 1; display: flex; align-items: center; justify-content: center; color: var(--accent-light); font-size: 30px; font-weight: 500; position: relative; }
  .tab.is-active::after { content: ""; position: absolute; left: 0; right: 0; bottom: 0; height: 7px; background: var(--accent); }

  .feed { padding: 0 22px; }
  .card { background: var(--card-bg); margin-top: 22px; padding: 22px 24px 0; box-shadow: 0 2px 4px rgba(0,0,0,.18); border-bottom: 6px solid var(--tag-colour); }
  .card:first-child { margin-top: 28px; }
  .card--movies { --tag-colour: var(--movies); }
  .card--running { --tag-colour: var(--accent); }
  .card--concert { --tag-colour: var(--concert); }
  .card--hiking { --tag-colour: var(--hiking); border-bottom: none; }
  .tag { font-size: 14px; font-weight: 500; color: var(--tag-colour); text-transform: uppercase; }
  .title { font-size: 31px; font-weight: 400; margin-top: 4px; }
  .stats { display: flex; margin: 18px 0 14px; }
  .stat { border-left: 2px solid var(--rule); padding-left: 12px; height: 58px; display: flex; flex-direction: column; justify-content: center; }
  .stat--person { width: 135px; }
  .stat--cost { width: 170px; }
  .stat--address { flex: 1; }
  .stat-label { font-size: 11px; color: var(--muted); text-transform: uppercase; }
  .stat-value { font-size: 20px; margin-top: 4px; }
  .footer { border-top: 1px solid var(--rule); display: flex; align-items: center; height: 72px; margin: 0 -24px; padding: 0 24px; }
  .avatar { width: 52px; height: 52px; border-radius: 50%; background: #f0f0f0; border: 2px solid #dcdcdc; }
  .poster { margin-left: 24px; width: 257px; }
  .poster-label, .when-day { font-size: 12px; color: var(--muted); }
  .poster-name, .when-time { font-size: 21px; margin-top: 3px; }
  .when-day { text-transform: uppercase; }

  .fab { position: absolute; left: 538px; top: 1118px; width: 106px; height: 106px; border-radius: 50%; background: var(--accent); box-shadow: 0 4px 8px rgba(0,0,0,.3); display: flex; align-items: center; justify-content: center; }
</style>
</head>
<body>
  <header>
    <div class="status-bar">
      <svg width="24" height="20" viewBox="0 0 24 20"><path d="M0 2 Q12 -4 24 2 L12 20 Z" fill="#fff"/></svg>
      <svg width="20" height="20" viewBox="0 0 20 20"><path d="M20 0 V20 H0 Z" fill="#fff" opacity=".5"/><path d="M12 8 V20 H0 Z" fill="#fff"/></svg>
      <svg width="12" height="22" viewBox="0 0 12 22"><rect x="3" y="0" width="6" height="2" fill="#fff"/><rect x="0" y="2" width="12" height="20" fill="#fff"/></svg>
      <span>12:30</span>
    </div>
    <div class="app-bar">
      <svg width="36" height="28" viewBox="0 0 36 28"><rect y="2" width="36" height="4" fill="#fff"/><rect y="12" width="36" height="4" fill="#fff"/><rect y="22" width="36" height="4" fill="#fff"/></svg>
      <span class="app-title">Activity App</span>
      <svg width="36" height="36" viewBox="0 0 36 36"><circle cx="14" cy="14" r="10" fill="none" stroke="#fff" stroke-width="4"/><line x1="21" y1="21" x2="33" y2="33" stroke="#fff" stroke-width="5"/></svg>
    </div>
    <nav class="tabs">
      <div class="tab is-active">Activities</div>
      <div class="tab">My Area</div>
    </nav>
  </header>

  <main class="feed">
    <article class="card card--movies">
      <p class="tag">#Movies</p>
      <h2 class="title">We're Going to the movies !</h2>
      <div class="stats">
        <div class="stat stat--person"><span class="stat-label">Person</span><span class="stat-value">3</span></div>
        <div class="stat stat--cost"><span class="stat-label">Cost</span><span class="stat-value">150 pesos</span></div>
        <div class="stat stat--address"><span class="stat-label">Address</span><span class="stat-value">Calle Verano Alto 14</span></div>
      </div>
      <div class="footer">
        <div class="avatar" role="img" aria-label="Poster profile picture"></div>
        <div class="poster"><p class="poster-label">Posted by :</p><p class="poster-name">Egar</p></div>
        <div class="when"><p class="when-day">Today</p><p class="when-time">8:00 PM</p></div>
      </div>
    </article>

    <article class="card card--running">
      <p class="tag">#Running</p>
      <h2 class="title">Running</h2>
      <div class="stats">
        <div class="stat stat--person"><span class="stat-label">Person</span><span class="stat-value">30</span></div>
        <div class="stat stat--cost"><span class="stat-label">Cost</span><span class="stat-value">70 pesos</span></div>
        <div class="stat stat--address"><span class="stat-label">Address</span><span class="stat-value">Brennmoor Lake walkway</span></div>
      </div>
      <div class="footer">
        <div class="avatar" role="img" aria-label="Poster profile picture"></div>
        <div class="poster"><p class="poster-label">Posted by :</p><p class="poster-name">Rega</p></div>
        <div class="when"><p class="when-day">Mon</p><p class="when-time">8:30 AM</p></div>
      </div>
    </article>

    <article class="card card--concert">
      <p class="tag">#Concert</p>
      <h2 class="title">Ironhowl Concert</h2>
      <div class="stats">
        <div class="stat stat--person"><span class="stat-label">Person</span><span class="stat-value">10</span></div>
        <div class="stat stat--cost"><span class="stat-label">Cost</span><span class="stat-value">1400 pesos</span></div>
        <div class="stat stat--address"><span class="stat-label">Address</span><span class="stat-value">Event Park</span></div>
      </div>
      <div class="footer">
        <div class="avatar" role="img" aria-label="Poster profile picture"></div>
        <div class="poster"><p class="poster-label">Posted by :</p><p class="poster-name">Adam</p></div>
        <div class="when"><p class="when-day">Friday</p><p class="when-time">10:00 PM</p></div>
      </div>
    </article>

    <article class="card card--hiking">
      <p class="tag">#Hiking</p>
      <h2 class="title">We're going to HIKING</h2>
    </article>
  </main>

  <a class="fab" aria-label="New activity">
    <svg width="40" height="40" viewBox="0 0 24 24"><path d="M3 17.25V21h3.75L17.8 9.94l-3.75-3.75L3 17.25zM20.7 7.04a1 1 0 0 0 0-1.41l-2.34-2.34a1 1 0 0 0-1.41 0l-1.83 1.83 3.75 3.75 1.83-1.83z" fill="#fff"/></svg>
  </a>
</body>
</html>
```